Buisness cards for international property developer
Morelli Costruzioni Group
Professional
Beatrice Solange Morelli
CEO
Head Office: Via Campo Lungo 158 00149 Rome Italy
beatrice.morelli@morellicostruzionigroup.com
www.morellicostruzionigroup.com

```html
<!DOCTYPE html>
<html lang="en">
<head>
<meta charset="utf-8">
<title>Morelli Costruzioni Group – Business Cards</title>
<link rel="stylesheet" href="https://fonts.googleapis.com/css2?family=Libre+Baskerville:wght@400;700&display=swap">
<style>
  :root {
    --backdrop: #3a3d40;
    --card: #ffffff;
    --ink: #1b1b1b;
    --gold: #c8923a;
    --gold-light: #e2b564;
    --band: #2a2a2a;
    --pattern-tone: #8a8a8a;
  }
  * { box-sizing: border-box; margin: 0; padding: 0; }
  html, body { width: 1200px; height: 857px; overflow: hidden; }
  body {
    background: var(--backdrop);
    font-family: "Libre Baskerville", Georgia, serif;
    color: var(--ink);
    position: relative;
  }
  .card {
    position: absolute;
    background: var(--card);
    box-shadow: 0 10px 30px rgba(0,0,0,.45);
  }
  /* Back side */
  .card-back { left: 110px; top: 170px; width: 340px; height: 520px; }
  .pattern-area {
    position: absolute; left: 50%; top: 50%;
    width: 230px; height: 230px;
    transform: translate(-50%, -50%) rotate(45deg);
    background: var(--pattern-tone);
  }
  .back-mark {
    position: absolute; left: 50%; top: 50%;
    transform: translate(-50%, -50%);
    width: 124px; padding: 12px 8px;
    background: var(--card);
    text-align: center;
  }
  .mark-square { display: block; width: 34px; height: 34px; margin: 0 auto 8px; background: var(--gold); }
  .mark-name {
    display: block; color: var(--gold); font-size: 10px; font-weight: 700;
    letter-spacing: .08em; text-transform: uppercase; line-height: 1.4;
  }
  /* Front side */
  .card-front { left: 540px; top: 250px; width: 560px; height: 360px; }
  .holder { position: absolute; left: 36px; top: 44px; }
  .holder-name { font-size: 21px; font-weight: 700; }
  .holder-role { font-size: 14px; font-weight: 700; margin-top: 6px; }
  .front-mark { position: absolute; right: 30px; top: 40px; width: 160px; text-align: center; }
  .divider {
    position: absolute; left: 270px; top: 150px;
    width: 2px; height: 110px; background: var(--ink);
  }
  .office {
    position: absolute; left: 300px; top: 160px;
    font-size: 14px; font-weight: 700; line-height: 1.6; font-style: normal;
  }
  .contact-band {
    position: absolute; left: 0; right: 0; bottom: 0; height: 40px;
    background: var(--band);
    display: flex; align-items: center; justify-content: center; gap: 18px;
    color: var(--gold-light); font-size: 10px; white-space: nowrap;
  }
  .contact-band .sep { width: 1px; height: 14px; background: var(--gold); }
</style>
</head>
<body>
  <section class="card card-back" aria-label="Card back">
    <div class="pattern-area" role="img" aria-label="Black and white geometric pattern set in a diamond"></div>
    <div class="back-mark">
      <span class="mark-square"></span>
      <span class="mark-name">Morelli Costruzioni Group</span>
    </div>
  </section>

  <section class="card card-front" aria-label="Card front">
    <div class="holder">
      <p class="holder-name">Beatrice Solange Morelli</p>
      <p class="holder-role">CEO</p>
    </div>
    <div class="front-mark">
      <span class="mark-square"></span>
      <span class="mark-name">Morelli Costruzioni Group</span>
    </div>
    <div class="divider"></div>
    <address class="office">
      Head Office:<br>
      Via Campo Lungo 158<br>
      00149 Rome<br>
      Italy
    </address>
    <footer class="contact-band">
      <span>beatrice.morelli@morellicostruzionigroup.com</span>
      <span class="sep"></span>
      <span>www.morellicostruzionigroup.com</span>
    </footer>
  </section>
</body>
</html>
```